Music teacher for flute, beinning piano and a Chime and Stride class

I would like a QP page where folks could contact me for flute and beginning piano lessons OR for a Chime and Stride class (low-impact exercises, singing, work with drumming/rhythms to alleviate the symptoms of Parkinson's disease.) I have a QP page for the Chime and Stride but not for music lessons.
https://www.pagelinkr.example/ChimeandStrideOakvale
I would want a different url since I am no longer doing this in Roseville, CA but Sacramento, CA

Hello, forgive me for dropping out of contact. Can you tell me if there was a fake QP page created under the username Chime and Stride Birchford? It's surprisingly close to what I offer but it says "Painting class" and other misinformation. Any information would be helpful, thanks. I'd like to switch my username to Chime and Stride Birchford, if possible.

```html
<!DOCTYPE html>
<html lang="en">
<head>
<meta charset="utf-8">
<title>Chime and Stride – QP Page</title>
<link href="https://fonts.googleapis.com/css2?family=Open+Sans:wght@400;600;700&family=Dancing+Script:wght@700&family=Merriweather:wght@700&family=Montserrat:wght@500;600;700&display=swap" rel="stylesheet">
<style>
:root{
  --page-white:#ffffff;
  --feed-grey:#f0f2f5;
  --control-grey:#e4e6eb;
  --divider:#ced0d4;
  --text-main:#050505;
  --text-muted:#65676b;
  --brand-blue:#1877f2;
  --like-tint:#e7f3ff;
  --badge-red:#e41e3f;
  --banner-black:#0c0c0c;
  --banner-gold:#eea81d;
  --avatar-cream:#fbe7a1;
  --leaf-green:#45bd62;
  --pin-red:#f3425f;
}
*{box-sizing:border-box;margin:0;padding:0}
html,body{width:1200px;height:1139px;overflow:hidden}
body{position:relative;background:var(--page-white);font-family:"Open Sans",sans-serif;color:var(--text-main)}
.abs{position:absolute}

/* top navigation */
.top-nav{left:0;top:0;width:1200px;height:71px;background:var(--page-white);border-top:3px solid var(--control-grey)}
.nav-icon{position:absolute;top:22px;width:34px;height:34px;margin-left:-17px}
.nav-badge{position:absolute;top:-6px;right:-10px;width:22px;height:22px;border-radius:50%;background:var(--badge-red);color:#fff;font-size:13px;font-weight:700;line-height:22px;text-align:center;border:2px solid #fff}

/* header backdrop */
.header-wash{left:0;top:71px;width:1200px;height:675px;background:linear-gradient(90deg,#eef5d6 0,#fff 30px,#fff 1170px,#f3f6de 1200px)}

/* banner */
.banner{left:24px;top:71px;width:1163px;height:443px;background:var(--banner-black);overflow:hidden}
.banner-photo{position:absolute;top:0;height:443px}
.photo-flute{left:0;width:380px;background:linear-gradient(90deg,#1a1a1a 0%,#3a3434 35%,#241f1f 65%,#0c0c0c 100%)}
.photo-piano{right:0;width:330px;background:linear-gradient(90deg,#0c0c0c 0%,#2a2326 40%,#3b3338 70%,#1b1a1f 100%)}
.banner-title{position:absolute;left:300px;width:560px;text-align:center;font-family:"Dancing Script",cursive;color:var(--banner-gold);font-size:100px;line-height:1}
.title-a{top:18px}
.title-b{top:112px}
.banner-tagline{position:absolute;left:500px;top:216px;font-family:"Merriweather",serif;font-weight:700;color:var(--banner-gold);font-size:27px}
.banner-rule{position:absolute;left:386px;width:438px;height:2px;background:var(--banner-gold)}
.banner-sub{position:absolute;left:386px;top:264px;width:438px;text-align:center;font-family:"Montserrat",sans-serif;font-weight:700;color:var(--banner-gold);font-size:20px;line-height:29px}
.lesson{position:absolute;font-family:"Montserrat",sans-serif;color:#fff;white-space:nowrap}
.lesson h3{font-size:20px;font-weight:600;letter-spacing:.2px;margin-bottom:6px}
.lesson p{font-size:14.5px;font-weight:600;line-height:22px}
.lesson-flute{left:227px;top:353px}
.lesson-piano{right:250px;top:350px;text-align:right}

/* page identity */
.page-avatar{left:80px;top:486px;width:166px;height:166px;border-radius:50%;background:var(--avatar-cream);border:4px solid #fff}
.page-name{left:268px;top:536px;font-size:34px;font-weight:700;letter-spacing:-.2px}
.page-meta{left:268px;top:585px;width:440px;font-size:20px;color:var(--text-muted);line-height:25px}
.btn-message{left:757px;top:588px;width:382px;height:48px;border-radius:7px;background:var(--brand-blue);color:#fff;font-size:20px;font-weight:600;display:flex;align-items:center;justify-content:center;gap:10px}
.btn-dot{width:18px;height:18px;border-radius:50%;background:#fff}

/* tabs */
.tab-rule{left:67px;top:672px;width:1072px;height:1px;background:var(--divider)}
.tab{top:698px;font-size:18px;font-weight:600;color:var(--text-muted)}
.tab-active{color:var(--brand-blue)}
.tab-underline{left:67px;top:741px;width:90px;height:4px;background:var(--brand-blue)}
.btn-like{left:843px;top:687px;width:159px;height:44px;border-radius:7px;background:var(--like-tint);color:var(--brand-blue);font-size:18px;font-weight:600;display:flex;align-items:center;justify-content:center}
.btn-square{top:687px;width:59px;height:44px;border-radius:7px;background:var(--control-grey);display:flex;align-items:center;justify-content:center}

/* feed */
.feed{left:0;top:746px;width:1200px;height:393px;background:var(--feed-grey);border-top:1px solid var(--divider)}
.card{background:#fff;border-radius:9px;box-shadow:0 1px 2px rgba(0,0,0,.18)}
.about-card{left:67px;top:766px;width:441px;height:400px;padding:18px 20px}
.about-head{display:flex;justify-content:space-between;align-items:baseline}
.about-head h2{font-size:24px;font-weight:700}
.see-all{font-size:18px;color:var(--brand-blue)}
.about-item{position:absolute;left:20px;display:flex;gap:14px;font-size:16.5px;line-height:23px;white-space:nowrap}
.info-icon{flex:none;width:22px;height:22px;border-radius:50%;background:#8a8d91;color:#fff;font-size:14px;font-weight:700;text-align:center;line-height:22px;margin-top:2px}
.see-more{font-weight:600}
.like-dot{flex:none;width:22px;height:22px;border-radius:50%;background:#8a8d91}

.compose-card{left:527px;top:766px;width:612px;height:142px}
.compose-avatar{position:absolute;left:18px;top:14px;width:50px;height:50px;border-radius:50%;background:linear-gradient(135deg,#fff3e6,#f2b47a);border:1px solid var(--divider)}
.online-dot{position:absolute;left:54px;top:50px;width:14px;height:14px;border-radius:50%;background:var(--leaf-green);border:2px solid #fff}
.compose-field{position:absolute;left:78px;top:14px;width:519px;height:49px;border-radius:7px;background:var(--control-grey);font-size:19px;font-weight:600;display:flex;align-items:center;justify-content:center}
.compose-action{position:absolute;top:90px;display:flex;align-items:center;gap:10px;font-size:18px;font-weight:600;color:var(--text-muted)}

.post-card{left:527px;top:927px;width:612px;height:240px;overflow:hidden}
.post-avatar{position:absolute;left:18px;top:14px;width:50px;height:50px;border-radius:50%;background:linear-gradient(135deg,#e4efb5,#8fc56a)}
.post-author{position:absolute;left:78px;top:14px;font-size:17.5px;font-weight:600}
.post-time{position:absolute;left:78px;top:39px;font-size:15px;color:var(--text-muted);display:flex;align-items:center;gap:5px}
.post-more{position:absolute;right:20px;top:22px}
.post-text{position:absolute;left:20px;top:72px;font-size:17.5px;line-height:23px;white-space:nowrap}
.post-link{color:var(--brand-blue)}
.post-photo{position:absolute;left:0;top:132px;width:612px;height:110px;background:linear-gradient(100deg,#1a0f10 0%,#3b1c1e 35%,#8c2c2c 60%,#2a1414 100%)}
</style>
</head>
<body>

<nav class="abs top-nav" aria-label="Main navigation">
  <div class="nav-icon" style="left:265px">
    <svg viewBox="0 0 34 34" width="34" height="34" fill="none" stroke="#65676b" stroke-width="2.4" stroke-linejoin="round"><path d="M5 16 17 6l12 10"/><path d="M8 14v14h7v-8h4v8h7V14"/></svg>
  </div>
  <div class="nav-icon" style="left:434px">
    <svg viewBox="0 0 34 34" width="34" height="34" fill="none" stroke="#65676b" stroke-width="2.4"><circle cx="13" cy="12" r="5"/><path d="M3 28c0-6 4-9 10-9s10 3 10 9z"/><circle cx="24" cy="11" r="4"/><path d="M24 18c4 0 8 2 8 8h-6"/></svg>
    <span class="nav-badge">5</span>
  </div>
  <div class="nav-icon" style="left:602px">
    <svg viewBox="0 0 34 34" width="34" height="34" fill="none" stroke="#65676b" stroke-width="2.4" stroke-linejoin="round"><rect x="4" y="6" width="26" height="19" rx="4"/><path d="M14 11v9l7-4.5z" fill="#65676b"/><path d="M9 29h16"/></svg>
    <span class="nav-badge">1</span>
  </div>
  <div class="nav-icon" style="left:771px">
    <svg viewBox="0 0 34 34" width="34" height="34" fill="none" stroke="#65676b" stroke-width="2.4" stroke-linejoin="round"><path d="M5 13 8 5h18l3 8"/><path d="M5 13c0 3 4 3 4 0 0 3 4 3 4 0 0 3 4 3 4 0 0 3 4 3 4 0 0 3 4 3 4 0 0 3 4 3 4 0"/><path d="M7 16v13h20V16"/><path d="M14 29v-7h6v7"/></svg>
  </div>
  <div class="nav-icon" style="left:938px">
    <svg viewBox="0 0 34 34" width="34" height="34" fill="none" stroke="#65676b" stroke-width="2.4"><circle cx="17" cy="17" r="14"/><circle cx="17" cy="14" r="3" fill="#65676b"/><circle cx="10" cy="17" r="2.4" fill="#65676b"/><circle cx="24" cy="17" r="2.4" fill="#65676b"/><path d="M11 25c1-4 4-6 6-6s5 2 6 6" fill="#65676b"/></svg>
    <span class="nav-badge">6</span>
  </div>
</nav>

<div class="abs header-wash"></div>

<header class="abs banner">
  <div class="banner-photo photo-flute" role="img" aria-label="Photo of a flautist performing on a dark stage"></div>
  <div class="banner-photo photo-piano" role="img" aria-label="Photo of a young woman playing a grand piano"></div>
  <div class="banner-title title-a">Chime &amp;</div>
  <div class="banner-title title-b">Stride</div>
  <div class="banner-tagline">Freedom of expression</div>
  <div class="banner-rule" style="top:259px"></div>
  <div class="banner-sub">USING MUSIC TO IMPROVE THE LIVES OF<br>FOLKS WITH PARKINSON'S DISEASE</div>
  <div class="banner-rule" style="top:329px"></div>
  <div class="lesson lesson-flute">
    <h3>FLUTE LESSON</h3>
    <p>Private lessons for all ages and levels<br>tone, breath and reading music made easy</p>
  </div>
  <div class="lesson lesson-piano">
    <h3>BEGINNING PIANO LESSONS</h3>
    <p>Start from zero with patient, friendly<br>lessons in scales, chords and songs</p>
  </div>
</header>

<div class="abs page-avatar" role="img" aria-label="Page profile emblem on a cream circle"></div>
<h1 class="abs page-name">Chime and Stride</h1>
<p class="abs page-meta">@ChimeandStrideBirchford · Sports &amp;<br>Recreation</p>
<div class="abs btn-message"><span class="btn-dot"></span>Send Message</div>

<div class="abs tab-rule"></div>
<span class="abs tab tab-active" style="left:87px">Home</span>
<span class="abs tab" style="left:176px">About</span>
<span class="abs tab" style="left:267px">Community</span>
<span class="abs tab" style="left:402px">Photos</span>
<span class="abs tab" style="left:500px">More
  <svg width="12" height="12" viewBox="0 0 12 12"><path d="M2 4h8L6 9z" fill="#65676b"/></svg></span>
<div class="abs tab-underline"></div>
<div class="abs btn-like">Like</div>
<div class="abs btn-square" style="left:1012px">
  <svg width="22" height="22" viewBox="0 0 22 22" fill="none" stroke="#050505" stroke-width="2.4"><circle cx="9" cy="9" r="6.5"/><path d="m14 14 6 6"/></svg>
</div>
<div class="abs btn-square" style="left:1080px">
  <svg width="22" height="6" viewBox="0 0 22 6" fill="#050505"><circle cx="3" cy="3" r="2.4"/><circle cx="11" cy="3" r="2.4"/><circle cx="19" cy="3" r="2.4"/></svg>
</div>

<main class="abs feed"></main>

<section class="abs card about-card">
  <div class="about-head"><h2>About</h2><span class="see-all">See All</span></div>
  <div class="about-item" style="top:86px">
    <span class="info-icon">i</span>
    <p>A low-impact, music-focused movement<br>class for the benefit of those with<br>Parkinson's,. Not only does music have<br>the power to enhance our lives emotion…<br><span class="see-more">See More</span></p>
  </div>
  <div class="about-item" style="top:220px">
    <span class="info-icon">i</span>
    <p>After being diagnosed with Parkinson's<br>Disease (PD) in 2015 and enrolling in<br>Steadfast Gym Oakvale in 2017, I wanted<br>to do something that joins… <span class="see-more">See More</span></p>
  </div>
  <div class="about-item" style="top:333px">
    <span class="like-dot"></span>
    <p>47 people like this</p>
  </div>
</section>

<section class="abs card compose-card">
  <div class="compose-avatar" role="img" aria-label="Small page emblem"></div>
  <span class="online-dot"></span>
  <div class="compose-field">Create Post</div>
  <div class="compose-action" style="left:44px">
    <svg width="24" height="24" viewBox="0 0 24 24"><rect x="2" y="3" width="20" height="18" rx="3" fill="#45bd62"/><circle cx="8" cy="9" r="2.2" fill="#fff"/><path d="M4 19l6-6 4 4 3-3 5 5z" fill="#fff"/></svg>Photo/Video
  </div>
  <div class="compose-action" style="left:252px">
    <svg width="24" height="24" viewBox="0 0 24 24"><path d="M12 2a7 7 0 0 0-7 7c0 5 7 13 7 13s7-8 7-13a7 7 0 0 0-7-7z" fill="#f3425f"/><circle cx="12" cy="9" r="2.6" fill="#fff"/></svg>Check in
  </div>
  <div class="compose-action" style="left:430px">
    <svg width="24" height="24" viewBox="0 0 24 24" fill="#1877f2"><circle cx="10" cy="7" r="4.5"/><path d="M1 21c0-5 4-8 9-8s9 3 9 8z"/><path d="M19 5v6M16 8h6" stroke="#1877f2" stroke-width="2.2"/></svg>Tag Friends
  </div>
</section>

<article class="abs card post-card">
  <div class="post-avatar" role="img" aria-label="Small page emblem"></div>
  <div class="post-author">Chime and Stride</div>
  <div class="post-time">3d ·
    <svg width="13" height="13" viewBox="0 0 13 13" fill="none" stroke="#65676b" stroke-width="1.4"><circle cx="6.5" cy="6.5" r="5.5"/><path d="M1 6.5h11M6.5 1c-3 3-3 8 0 11M6.5 1c3 3 3 8 0 11"/></svg>
  </div>
  <svg class="post-more" width="22" height="6" viewBox="0 0 22 6" fill="#65676b"><circle cx="3" cy="3" r="2.4"/><circle cx="11" cy="3" r="2.4"/><circle cx="19" cy="3" r="2.4"/></svg>
  <p class="post-text">From <span class="post-link">TuneDigest.example</span>. Crimson Valley Revival drummer Dale<br>Corbin gets behind his drum kit every day...even with his Parkinson's.</p>
  <div class="post-photo" role="img" aria-label="Concert photo of a drummer on stage under red lights"></div>
</article>

</body>
</html>
```